PLOVEN Business Card

Coastal Build Additions and Refits. I need a business card designed for this new high end renovation business. I would like the logo centered on the back side with the ABN (37 915 402 176) on the bottom right hand corner.

I would like the following information placed on the other side along with some customized pattern or design.

Derek Collwood
Director
Phone: 1300 480 957
Fax: (02) 8145 9021
Website: www.plovenbuilders.com.au
Email: d.collwood@plovenbuilders.com.au
PO Box 87,
Kelvinbrook NSW 2069

(FB Logo) PLOVEN - Coastal Build Additions and Refits

The final design should communicate professionalism and trust.

Back side background colour: white
Front side: Undecided

```html
<!DOCTYPE html>
<html lang="en">
<head>
<meta charset="utf-8">
<title>PLOVEN Business Card</title>
<link rel="stylesheet" href="https://fonts.googleapis.com/css2?family=Crimson+Text:wght@400;600&display=swap">
<style>
  :root {
    --stage: #e4e5e6;
    --brand-blue: #1a5f8c;
    --charcoal: #3e3e40;
    --paper: #f5f6f6;
    --white: #ffffff;
    --ink: #333335;
  }
  * { margin: 0; padding: 0; box-sizing: border-box; }
  html, body {
    width: 1200px; height: 437px; overflow: hidden;
    background: var(--stage);
    font-family: "Crimson Text", Georgia, serif;
  }
  .canvas { position: relative; width: 1200px; height: 437px; }
  .card {
    position: absolute; top: 83px; width: 507px; height: 289px; overflow: hidden;
  }
  .card--front { left: 47px; background: var(--brand-blue); }
  .card--back { left: 614px; background: var(--paper); }
  .band { position: absolute; left: 0; width: 100%; }
  .card--front .band { top: 95px; height: 36px; }
  .card--back .band { top: 199px; height: 33px; }
  .band svg { display: block; width: 100%; height: 100%; }
  .band-text {
    position: absolute; top: 0; height: 100%;
    display: flex; align-items: center; justify-content: center;
    font-size: 19px; letter-spacing: 0.3px;
  }
  .holder-name { left: 0; width: 282px; color: var(--white); }
  .holder-role { left: 300px; width: 207px; color: var(--ink); }
  .abn { left: 240px; width: 267px; color: var(--white); font-size: 18px; letter-spacing: 0.6px; }
  .contact {
    position: absolute; top: 143px; left: 0; width: 100%;
    text-align: center; color: var(--white); font-size: 15.5px; line-height: 20.5px;
  }
  .contact b { font-weight: 600; }
  .contact .gap { display: inline-block; width: 20px; }
  .brand-panel {
    position: absolute; left: 80px; top: 83px; width: 349px; height: 114px;
    background: var(--white);
    display: flex; flex-direction: column; align-items: center; justify-content: center;
  }
  .brand-name {
    font-size: 58px; line-height: 1; font-weight: 400; color: var(--charcoal);
    letter-spacing: 1px;
  }
  .brand-tagline {
    display: flex; align-items: center; gap: 6px; margin-top: 8px;
    color: var(--brand-blue); font-size: 13.5px; letter-spacing: 0.8px; text-transform: uppercase;
  }
  .brand-tagline::before, .brand-tagline::after {
    content: ""; width: 14px; height: 1.5px; background: var(--brand-blue);
  }
</style>
</head>
<body>
<main class="canvas">
  <section class="card card--front" aria-label="Card front">
    <div class="band">
      <svg viewBox="0 0 507 36" preserveAspectRatio="none" aria-hidden="true">
        <polygon points="0,0 264,0 243,36 0,36" fill="var(--charcoal)"/>
        <polygon points="273,0 507,0 507,36 252,36" fill="var(--paper)"/>
      </svg>
      <span class="band-text holder-name">Derek Collwood</span>
      <span class="band-text holder-role">Director</span>
    </div>
    <address class="contact">
      <b>T:</b> 1300 480 957<span class="gap"></span><b>F:</b> (02) 8145 9021<br>
      PO Box 87, Kelvinbrook NSW 2069<br>
      <b>E:</b> d.collwood@plovenbuilders.com.au<br>
      <b>W:</b> www.plovenbuilders.com.au
    </address>
  </section>

  <section class="card card--back" aria-label="Card back">
    <div class="brand-panel">
      <span class="brand-name">PLOVEN</span>
      <span class="brand-tagline">Coastal Build Additions &amp; Refits</span>
    </div>
    <div class="band">
      <svg viewBox="0 0 508 33" preserveAspectRatio="none" aria-hidden="true">
        <polygon points="0,0 264,0 239,33 0,33" fill="var(--charcoal)"/>
        <polygon points="267,0 508,0 508,33 243,33" fill="var(--brand-blue)"/>
      </svg>
      <span class="band-text abn">ABN (37 915 402 176)</span>
    </div>
  </section>
</main>
</body>
</html>
```